Pine Arbor Table & Chair Rentals

We need a business card for a table and chair rental company. We rent tables and chairs for weddings, funerals, business events and parties. We want something that looks clean and elegant while not being too busy. We would like colors in the green and blue hues and avoiding anything orange. We want to make sure the font is large enough to be seen easily.

Target Market(s)

Wedding & Event Rentals

Industry/Entity Type

Events

Contact Information for Business Card

Pine Arbor, sales@pinearborrentals.example, pinearborrentals.example, 555-218-0937

Requirements
Must have
• Easy to read font
Should not have
• Orange anywhere in the design

```html
<!DOCTYPE html>
<html lang="en">
<head>
<meta charset="utf-8">
<title>Pine Arbor Table &amp; Chair Rentals – Business Card</title>
<link href="https://fonts.googleapis.com/css2?family=Ubuntu:wght@400;500&display=swap" rel="stylesheet">
<style>
  :root {
    --bg: #ece8e1;
    --green: #6e9a35;
    --green-dark: #587f28;
    --yellow: #f2cf2e;
    --yellow-deep: #e8c31f;
    --yellow-light: #f5d843;
    --stripe-dark: #3b3622;
    --paper: #fbfbf9;
    --ink: #3a3a36;
    --white: #ffffff;
  }
  * { margin: 0; padding: 0; box-sizing: border-box; }
  html, body { width: 1200px; height: 885px; overflow: hidden; }
  body {
    background: var(--bg);
    font-family: "Ubuntu", "Helvetica Neue", Arial, sans-serif;
    position: relative;
  }
  .card {
    position: absolute;
    left: 250px;
    width: 700px;
    height: 400px;
    border-radius: 4px;
    overflow: hidden;
    box-shadow: 0 6px 18px rgba(0,0,0,0.18);
  }
  .card--front { top: 30px; }
  .card--back { top: 455px; }
  .card__art { position: absolute; inset: 0; width: 100%; height: 100%; }

  .brand { position: absolute; color: var(--white); font-weight: 400; }
  .card--front .brand { right: 28px; top: 26px; text-align: right; }
  .brand__name { font-size: 44px; line-height: 1.05; }
  .brand__tagline { font-size: 22px; margin-top: 4px; }

  .contact { position: absolute; left: 40px; top: 150px; color: var(--ink); }
  .contact__name { font-size: 40px; font-weight: 500; margin-bottom: 10px; }
  .contact__list { list-style: none; font-size: 20px; }
  .contact__item { display: flex; align-items: center; gap: 10px; margin-bottom: 5px; }
  .contact__icon { width: 20px; height: 20px; flex: none; }

  .location {
    position: absolute; right: 34px; top: 205px;
    font-size: 19px; color: var(--ink);
  }

  .card--back .brand { left: 60px; top: 95px; }
  .card--back .brand__name { font-size: 54px; }
  .card--back .brand__tagline { font-size: 26px; }
  .web { position: absolute; left: 60px; top: 270px; color: var(--white); font-size: 26px; }
</style>
</head>
<body>

  <section class="card card--front" aria-label="Business card front">
    <svg class="card__art" viewBox="0 0 700 400" preserveAspectRatio="none" aria-hidden="true">
      <defs>
        <linearGradient id="greenFront" x1="0" y1="0" x2="1" y2="1">
          <stop offset="0" stop-color="#7aa83e"/>
          <stop offset="1" stop-color="#5f8a2b"/>
        </linearGradient>
      </defs>
      <rect width="700" height="400" fill="url(#greenFront)"/>
      <path d="M0,30 C220,35 380,155 700,145 L700,340 C430,345 260,385 0,382 Z" fill="var(--yellow)"/>
      <path d="M0,40 C220,45 380,165 700,155 L700,330 C430,335 260,375 0,372 Z" fill="var(--stripe-dark)"/>
      <path d="M0,50 C220,55 380,175 700,165 L700,320 C430,325 260,365 0,362 Z" fill="var(--paper)"/>
    </svg>

    <div class="brand">
      <div class="brand__name">Pine Arbor</div>
      <div class="brand__tagline">Table and Chair Rentals</div>
    </div>

    <div class="location">Alderwood Bay, Washington</div>

    <div class="contact">
      <div class="contact__name">Pine Arbor</div>
      <ul class="contact__list">
        <li class="contact__item">
          <svg class="contact__icon" viewBox="0 0 20 20" aria-hidden="true"><rect width="20" height="20" rx="4" fill="var(--ink)"/><path d="M6 4.5 L8.2 4.5 L9 7.5 L7.6 8.6 C8.3 10.2 9.6 11.6 11.3 12.4 L12.4 11 L15.5 11.8 L15.5 14 C15.5 14.8 14.8 15.5 14 15.5 C8.8 15.2 4.8 11.2 4.5 6 C4.5 5.2 5.2 4.5 6 4.5 Z" fill="#fff"/></svg>
          555-218-0937
        </li>
        <li class="contact__item">
          <svg class="contact__icon" viewBox="0 0 20 20" aria-hidden="true"><rect width="20" height="20" rx="4" fill="var(--ink)"/><rect x="4" y="6" width="12" height="8.5" fill="none" stroke="#fff" stroke-width="1.4"/><path d="M4 6 L10 11 L16 6" fill="none" stroke="#fff" stroke-width="1.4"/></svg>
          sales@pinearborrentals.example
        </li>
        <li class="contact__item">
          <svg class="contact__icon" viewBox="0 0 20 20" aria-hidden="true"><rect width="20" height="20" rx="10" fill="var(--ink)"/><g fill="none" stroke="#fff" stroke-width="1.2"><circle cx="10" cy="10" r="6"/><ellipse cx="10" cy="10" rx="2.6" ry="6"/><path d="M4 10 H16 M5 7 H15 M5 13 H15"/></g></svg>
          www.pinearborrentals.example
        </li>
      </ul>
    </div>
  </section>

  <section class="card card--back" aria-label="Business card back">
    <svg class="card__art" viewBox="0 0 700 400" preserveAspectRatio="none" aria-hidden="true">
      <defs>
        <linearGradient id="yellowBack" x1="0" y1="0" x2="1" y2="1">
          <stop offset="0" stop-color="var(--yellow-deep)"/>
          <stop offset="0.6" stop-color="var(--yellow-light)"/>
          <stop offset="1" stop-color="var(--yellow)"/>
        </linearGradient>
      </defs>
      <rect width="700" height="400" fill="url(#yellowBack)"/>
      <path d="M0,0 L46,0 C24,150 70,290 36,400 L0,400 Z" fill="var(--green)"/>
      <path d="M0,0 L32,0 C12,150 58,290 24,400 L0,400 Z" fill="var(--paper)"/>
      <path d="M0,0 L22,0 C4,150 48,290 14,400 L0,400 Z" fill="var(--stripe-dark)"/>
      <path d="M0,0 L10,0 C-4,150 36,290 4,400 L0,400 Z" fill="var(--green-dark)"/>
      <path d="M700,0 L540,0 C580,120 500,280 600,400 L700,400 Z" fill="var(--stripe-dark)"/>
      <path d="M700,0 L552,0 C592,120 512,280 612,400 L700,400 Z" fill="var(--paper)"/>
      <path d="M700,0 L566,0 C606,120 526,280 626,400 L700,400 Z" fill="var(--green)"/>
    </svg>

    <div class="brand">
      <div class="brand__name">Pine Arbor</div>
      <div class="brand__tagline">Table and Chair Rentals</div>
    </div>
    <div class="web">www.pinearborrentals.example</div>
  </section>

</body>
</html>
```